TembaLinkHub

Hey

I am involved with crowd funding, please look at one of my current sites www.fundvessel.net
Work is currently under way with a new site www.tembalinkhub.com .wehave the basics but I am not happy with what we have so far. I need to redesign the web site but keep the concept . The cartoon pitch will be kept , along with some of the other functions which we can help you with, unless you are able to build / design something better. I liked a lot of the designs submitted for a previous crowd funning design, far better than what I currently have. To be included on this site will be links to numerous crowd funding sites which I have registered but each site will be focused on a specific topic which will be disclosed once this site is active. I intend to build all these sites through this site. Along with these sites will be a logo design for each site so plenty of work going forward. I have a logo for tembalinkhub already but am open for improvements and suggestions but would like to keep a map or logo of Africa included in the design. To bear in mind this is a African focused buisness which aims to help communities, employment creation, poverty alleviation and help young entrepreneurs kickstarter their buisness . I already have a group logo , which was designed on this site ( look at ubuntu harvests competition) , I would like this logo to be used on all the site so customers and investors link the group and concept togeather. Here is the link http://www.sketchbazaar.example/project-progress.aspx?briefId=48213 . I have removed the ubuntuharvest from the bottom of the logo and will just be using the figurines as the group logo on all web sites. There will be at least fifty related crowd fund projects linked to this site.
If any body has any questions or ideas please feel free to ask for anything you may need. Thanks to everybody who helps with this project. Warmly. Owen

Hi everyone working on my design.

The contact details to use on the site are

27 Velden Close
Kelwater
Cape Town 
+263719483025
+447500294318

E mail enquiries@TembaLinkHub.example

There are two logos, one is the tembalinkhub logo and the other is my group logo which I will attach to the pitch
Good luck and thank you to everybody who is working on this web design
Warmly

Owen

```html
<!DOCTYPE html>
<html lang="en">
<head>
<meta charset="utf-8">
<title>TembaLinkHub – Equity Crowdfunding</title>
<link href="https://fonts.googleapis.com/css2?family=Arimo:wght@400;700&family=Oswald:wght@400&display=swap" rel="stylesheet">
<style>
:root{
  --olive:#6b7d1f;
  --olive-dark:#56661a;
  --blue:#1b5a99;
  --blue-dark:#0f3e6f;
  --navy:#1a4a8a;
  --red:#d62a2f;
  --red-dark:#b81d22;
  --tan:#b5a06a;
  --bg:#efefef;
  --line:#d9d9d9;
  --text:#333333;
  --muted:#666666;
  --brown:#4b3a2a;
  --brown-dark:#2e2419;
  --cream:#e6e1d3;
  --footer-text:#e8e2d8;
  --footer-line:#6a5640;
}
*{box-sizing:border-box;margin:0;padding:0}
html,body{width:943px;height:1200px;overflow:hidden}
body{font-family:"Arimo",Arial,sans-serif;background:var(--bg);color:var(--text);position:relative;font-size:10px}
a{color:inherit;text-decoration:none}
.abs{position:absolute}

.topbar{left:0;top:0;width:943px;height:26px;background:var(--olive)}
.topbar-links{left:324px;top:0;width:444px;height:26px;background:var(--olive-dark);color:#fff;font-size:8px;font-weight:700;display:flex;align-items:center;justify-content:space-between;padding:0 8px;white-space:nowrap}
.header{left:0;top:26px;width:943px;height:82px;background:#fff;border-top:3px dotted #cbb98a}

.brand{left:178px;top:46px;display:flex;align-items:center;gap:8px}
.brand-mark{width:38px;height:38px;border-radius:50%;background:#7fb42b}
.brand-name{font-size:21px;font-weight:700;color:var(--navy)}
.brand-tag{left:292px;top:74px;font-size:6.5px;font-weight:700;color:var(--text);letter-spacing:.3px}

.btn-top{top:34px;height:19px;border-radius:3px;color:#fff;font-size:8px;font-weight:700;display:flex;align-items:center;justify-content:center;white-space:nowrap}
.btn-social{left:446px;width:112px;background:#3d5a98}
.btn-signup{left:564px;width:60px;background:#7d9530}
.btn-login{left:631px;width:89px;background:#7d9530}
.group-mark{left:734px;top:30px;width:28px;height:28px;border-radius:50%;background:#8b3fa0}
.phones{left:690px;top:62px;font-size:8px;line-height:11px;font-weight:700;letter-spacing:.5px}
.phone-icon{left:670px;top:65px;width:14px;height:14px;border-radius:50%;background:#2a8bd0}
.email{left:628px;top:88px;font-size:8px;font-weight:700;display:flex;gap:4px;align-items:center;white-space:nowrap}

.nav{left:0;top:108px;width:943px;height:27px;background:linear-gradient(#2a70b5,var(--blue-dark))}
.nav ul{list-style:none;display:flex;position:absolute;left:178px;top:0;height:27px;align-items:center;color:#fff;font-size:9px;font-weight:700}
.nav li{padding:0 10px;border-right:1px solid rgba(255,255,255,.5)}
.nav li:last-child{border:none}
.nav li.active{background:#3d84c6;padding:5px 6px;border:none;margin-right:10px}
.search{left:612px;top:113px;width:149px;height:17px;background:#fff;border-radius:2px;font-size:9px;color:#666;padding:3px 6px}

.hero{left:176px;top:146px;width:590px;height:176px;background:#fff;border:1px solid #ddd;box-shadow:0 2px 3px rgba(0,0,0,.15)}
.hero-text{left:4px;top:4px;width:304px;height:166px;background:#f1eee6;padding:16px 18px}
.hero-text h2{font-size:12px;margin-bottom:8px}
.hero-text p{font-size:11.5px;line-height:16px}
.hero-text .join{color:var(--red);font-weight:700}
.pill{border-radius:10px;color:#fff;font-size:8px;font-weight:700;display:flex;align-items:center;justify-content:center;height:18px}
.pill-tan{background:var(--tan)}
.pill-red{background:var(--red)}
.hero-photo{left:308px;top:4px;width:278px;height:166px;background:linear-gradient(135deg,#9aa3ae,#3b3f46 55%,#c9ccd1)}

.welcome{left:0;top:328px;width:943px;text-align:center;font-size:21px;font-weight:700;color:var(--navy)}

.intro-band{left:0;top:355px;width:943px;height:174px;background:#f7f7f7;border-top:1px solid var(--line);border-bottom:1px solid var(--line)}
.intro h3{font-size:15px;font-weight:700;margin-bottom:6px}
.intro p{font-size:9.5px;line-height:13px;color:var(--muted);text-align:justify}
.intro .watch{font-weight:700;color:var(--navy);font-size:9px;margin-top:2px}
.video{left:373px;top:382px;width:192px;height:122px;background:linear-gradient(#8d8d8d,#4f4f4f);border:2px solid #333}
.video-bar{left:0;bottom:0;width:100%;height:10px;background:#222}
.promo{color:#fff;padding:8px 10px}
.promo h4{font-family:"Oswald","Arial Narrow",sans-serif;font-weight:400;font-size:18px;margin-bottom:3px;line-height:22px}
.promo p{font-size:8.5px;line-height:10.5px;width:122px}
.join-box{left:592px;top:382px;width:172px;height:122px;background:linear-gradient(#e2353a,var(--red-dark));border-radius:3px}
.join-box .tab{right:0;bottom:0;width:62px;height:22px;background:#a81a1e;border-radius:12px 0 0 0;font-size:8px;font-weight:700;display:flex;align-items:center;justify-content:center}

.card{width:186px;background:#fff;border:1px solid var(--line);box-shadow:0 1px 2px rgba(0,0,0,.12)}
.card-head{height:28px;background:linear-gradient(#e0393d,var(--red-dark));color:#fff;font-size:10px;text-align:center;line-height:28px}
.card-body{padding:10px 11px 6px;height:96px}
.card-body h5{color:var(--navy);font-size:9.5px;margin-bottom:8px}
.card-body p{font-size:8.5px;line-height:11px;color:var(--text)}
.more{display:inline-block;margin-top:4px;border:1px solid #bbb;border-radius:3px;background:#eee;padding:1px 7px;font-size:7.5px}
.stat{height:22px;border-top:1px solid var(--line);display:flex;align-items:center;padding:0 7px;font-size:9px}
.stat.backers{height:30px;background:#f5f5f5;font-size:14px}
.stat .lbl{color:var(--red);width:36px}
.people{width:24px;height:10px;background:#6b7d1f;border-radius:5px 5px 0 0;margin-right:20px}

.fund-box{left:592px;top:544px;width:172px;height:104px;background:linear-gradient(#7d9530,#5d7019);border-radius:3px;padding:6px 10px}
.fund-box .read{font-style:italic;font-weight:700;font-size:8.5px;margin-top:3px;line-height:10px}
.fund-corner{right:0;top:0;width:54px;height:54px;background:#fff;clip-path:polygon(0 0,100% 0,100% 100%)}
.fund-coin{right:6px;top:6px;width:26px;height:26px;border-radius:50%;background:var(--olive)}

.cat-title{left:592px;top:662px;font-size:11.5px;font-weight:700;color:var(--navy)}
.cat-rule{left:592px;top:682px;width:172px;height:3px;background:var(--line)}
.cat-rule::before{content:"";position:absolute;left:0;top:0;width:52px;height:3px;background:var(--blue)}
.cat-box{left:592px;top:696px;width:172px;height:244px;background:var(--cream);padding:16px 14px}
.cat-box ul{list-style:none}
.cat-box li{font-size:8.5px;height:17.8px;border-bottom:1px solid #cfc8b5;border-left:2px solid var(--blue);padding-left:4px;width:102px;line-height:16px}
.cat-box li.strong{font-weight:700}

.footer{left:0;top:972px;width:943px;height:204px;background:var(--brown);border-top:4px dotted #c9a65a}
.landscape{left:0;top:1090px;width:943px;height:86px;background:linear-gradient(transparent,var(--brown-dark) 70%)}
.foot-col{color:var(--footer-text);font-size:8.5px;z-index:2}
.foot-col h6{font-size:10.5px;color:#fff;font-weight:700;margin-bottom:12px}
.link-grid{display:grid;grid-template-columns:80px 80px}
.link-grid span{height:19px;border-bottom:1px solid var(--footer-line);line-height:18px;white-space:nowrap}
.contact-list span{display:block;height:19px;border-bottom:1px solid var(--footer-line);line-height:18px;width:172px;white-space:nowrap}
.field{background:#fff;color:#444;font-size:8px;padding:3px 10px;height:17px;margin-bottom:4px;border:1px solid #999;width:195px}
.field.msg{height:36px}
.submit{width:72px;margin-left:123px;margin-top:8px}
.badge{top:1128px;height:30px;z-index:2}
.social{left:610px;top:1138px;display:flex;gap:3px;z-index:2}
.social i{display:block;width:17px;height:17px;border-radius:2px}
.copy{left:0;top:1176px;width:943px;height:24px;background:#1d1712;color:#ddd;font-size:8.5px;text-align:center;line-height:24px}
.copy b{color:#fff;text-decoration:underline}
</style>
</head>
<body>

<div class="abs topbar"></div>
<div class="abs topbar-links">
  <span>Blogs | IPO's | How it Works | About TembaLinkHub</span>
  <span>Welcome Guest! &nbsp; My Account | Wishlist | Register &nbsp;Sign In</span>
</div>

<div class="abs header"></div>
<div class="abs brand"><span class="brand-mark"></span><span class="brand-name">TEMBALINKHUB</span></div>
<div class="abs brand-tag">EQUITY CROWDFUNDING</div>
<a class="abs btn-top btn-social">Sign In with Peerlink</a>
<a class="abs btn-top btn-signup">Sign Up Today</a>
<a class="abs btn-top btn-login">Login to your Account</a>
<div class="abs group-mark" role="img" aria-label="Group logo"></div>
<div class="abs phone-icon"></div>
<div class="abs phones">+263719483025<br>+447500294318</div>
<div class="abs email">
  <svg width="12" height="9" viewBox="0 0 12 9"><rect x=".5" y=".5" width="11" height="8" fill="none" stroke="#333"/><path d="M.5 .5 6 5l5.5-4.5" fill="none" stroke="#333"/></svg>
  enquiries@TembaLinkHub.example
</div>

<nav class="abs nav">
  <ul>
    <li class="active">Home</li><li>Company Info</li><li>Join Now!</li><li>How it works?</li><li>Browse Companies</li>
  </ul>
</nav>
<div class="abs search">search...</div>

<section class="abs hero">
  <div class="abs hero-text">
    <h2>Ground rules are simple</h2>
    <p><span class="join">JOIN</span>, send us a ClipStream or any other video link to any idea. It can be an idea just floating around or an idea which has already come to life. No catches, no entry fee, no award collection fee, only one entry per member.</p>
    <a class="abs pill pill-tan" style="left:18px;top:136px;width:72px">Learn more</a>
  </div>
  <div class="abs hero-photo" role="img" aria-label="Photo of two business people talking"></div>
</section>

<h1 class="abs welcome">Welcome to Africa’s leading crowdfunding site</h1>

<div class="abs intro-band"></div>
<div class="abs intro" style="left:176px;top:374px;width:174px">
  <h3>What is Crowdfunding?</h3>
  <p>Crowdfunding enables people to raise money for innovative new projects by getting like-minded individuals to pool their money to back the idea, person or business. It's a way to make things happen.</p>
  <div class="watch">WATCH THE VIDEO</div>
</div>
<a class="abs pill pill-tan" style="left:190px;top:497px;width:70px">Learn more here</a>
<a class="abs pill pill-red" style="left:271px;top:497px;width:72px">Join Now!</a>
<div class="abs video" role="img" aria-label="Cartoon pitch video"><div class="abs video-bar"></div></div>
<div class="abs join-box promo">
  <h4>JOIN NOW!</h4>
  <p>Adipiscing elit. Curabitur eu interdum dui. Aliquam turpis mauris, rhoncus et tempus ac, pellentesque quis sem. Nullam a leo arcu, in posuere leo.</p>
  <div class="abs tab">Join Now!</div>
</div>

<article class="abs card" style="left:178px;top:544px">
  <div class="card-head">Russia</div>
  <div class="card-body"><h5>Lorem ipsum dolor sit amet,</h5><p>Adipiscing elit. Curabitur eu interdum dui. Aliquam turpis mauris, rhoncus et tempus ac, pellentesque quis sem. Nullam a leo arcu, in posuere leo.</p><span class="more">more</span></div>
  <div class="stat backers"><span class="people"></span>0</div>
  <div class="stat"><span class="lbl">Funded</span>$0.00</div>
  <div class="stat"><span class="lbl">Goal</span>$3000.00</div>
</article>
<article class="abs card" style="left:378px;top:544px">
  <div class="card-head">Middle East</div>
  <div class="card-body"><h5>Lorem ipsum dolor sit amet,</h5><p>Adipiscing elit. Curabitur eu interdum dui. Aliquam turpis mauris, rhoncus et tempus ac, pellentesque quis sem. Nullam a leo arcu, in posuere leo.</p><span class="more">more</span></div>
  <div class="stat backers"><span class="people"></span>0</div>
  <div class="stat"><span class="lbl">Funded</span>$0.00</div>
  <div class="stat"><span class="lbl">Goal</span>$3000.00</div>
</article>
<article class="abs card" style="left:178px;top:748px">
  <div class="card-head">Eastern Europe</div>
  <div class="card-body"><h5>Lorem ipsum dolor sit amet,</h5><p>Adipiscing elit. Curabitur eu interdum dui. Aliquam turpis mauris, rhoncus et tempus ac, pellentesque quis sem. Nullam a leo arcu, in posuere leo.</p><span class="more">more</span></div>
  <div class="stat backers"><span class="people"></span>0</div>
  <div class="stat"><span class="lbl">Funded</span>$0.00</div>
  <div class="stat"><span class="lbl">Goal</span>$3000.00</div>
</article>
<article class="abs card" style="left:378px;top:748px">
  <div class="card-head">Gache Gache Reserve, Zimbabwe</div>
  <div class="card-body"><h5>Lorem ipsum dolor sit amet,</h5><p>Adipiscing elit. Curabitur eu interdum dui. Aliquam turpis mauris, rhoncus et tempus ac, pellentesque quis sem. Nullam a leo arcu, in posuere leo.</p><span class="more">more</span></div>
  <div class="stat backers"><span class="people"></span>5</div>
  <div class="stat"><span class="lbl">Funded</span>$5.00</div>
  <div class="stat"><span class="lbl">Goal</span>$100.00</div>
</article>

<div class="abs fund-box promo">
  <div class="abs fund-corner"></div><div class="abs fund-coin"></div>
  <h4>FUND</h4>
  <p>Adipiscing elit. Curabitur eu interdum dui. Aliquam turpis mauris, rhoncus et tempus ac, pellentesque quis sem. Nullam a leo arcu, in posuere leo.</p>
  <div class="read">Read more...</div>
</div>

<div class="abs cat-title">Business Categories</div>
<div class="abs cat-rule"></div>
<div class="abs cat-box">
  <ul>
    <li>Comics</li><li>Environment</li><li>Fashion</li><li>Film &amp; Video</li><li>Gaming</li><li>Health &amp; Fitness</li><li>Music</li><li>Professional Services</li><li>Technology</li><li>More links</li><li class="strong">Internet &amp; IT</li><li>Leasure &amp; Tourism</li>
  </ul>
</div>

<footer class="abs footer"></footer>
<div class="abs landscape" role="img" aria-label="Silhouette of African savanna with animals"></div>
<div class="abs foot-col" style="left:178px;top:998px">
  <h6>About Us</h6>
  <div class="link-grid">
    <span>About US</span><span>Resources</span><span>Join Now</span><span>FAQ</span><span>How it works</span><span>Email Us</span><span>Privacy policy</span><span>My Account</span><span>Our Blog</span><span>Sign Up now</span>
  </div>
</div>
<div class="abs foot-col contact-list" style="left:376px;top:998px">
  <h6>Contact Us</h6>
  <span>Phone: +263719483025</span><span>Fax: &nbsp;&nbsp;&nbsp;&nbsp;+447500294318</span><span>enquiries@TembaLinkHub.example</span><span>27 Velden Close, Kelwater, Cape Town</span>
</div>
<div class="abs foot-col" style="left:571px;top:998px">
  <h6>Comments &amp; Feedback</h6>
  <div class="field">Enter your name</div>
  <div class="field">Enter your email here</div>
  <div class="field msg">Message</div>
  <a class="pill pill-red submit">Submit</a>
</div>
<div class="abs badge" style="left:178px;width:116px;background:#3f8a2a;border-radius:15px 4px 4px 15px" role="img" aria-label="Accreditation badge"></div>
<div class="abs badge" style="left:304px;width:76px;background:#f2f2f2;border-radius:3px" role="img" aria-label="Privacy certification badge"></div>
<div class="abs badge" style="left:398px;width:60px;background:#f2f2f2;border-radius:15px" role="img" aria-label="Security badge"></div>
<div class="abs social" role="img" aria-label="Social links">
  <i style="background:#3d5a98"></i><i style="background:#2aa3d8"></i><i style="background:#1478b5"></i><i style="background:#c8232c"></i><i style="background:#d84a38"></i><i style="background:#cccccc"></i><i style="background:#2aa14c"></i>
</div>
<div class="abs copy">Copyright 2012 TembaLinkHub &nbsp;/ &nbsp; Use of this website constitutes acceptance of our <b>User Agreement</b> and <b>Privacy Policy</b></div>

</body>
</html>
```